Stationery Design Project

Require letterhead/stationery design based on new logo (see attached).

Would prefer it kept simple but strong and effective.

Target Market(s)

Clients and building developers. Residential/consumer and corporate clientele.

```html
<!DOCTYPE html>
<html lang="en">
<head>
<meta charset="utf-8">
<title>Stratafold Projects – Letterhead</title>
<link rel="stylesheet" href="https://fonts.googleapis.com/css2?family=Source+Sans+3:wght@400;600&display=swap">
<style>
  :root {
    --paper: #ffffff;
    --accent: #29abe2;
    --ink-grey: #58595b;
    --brand-grey: #6d6e71;
    --mark-tint: #edf7fc;
    --mark-ring: #e6e7e8;
  }
  * { margin: 0; padding: 0; box-sizing: border-box; }
  html, body {
    width: 848px;
    height: 1200px;
    overflow: hidden;
    background: var(--paper);
  }
  .letterhead {
    position: relative;
    width: 848px;
    height: 1200px;
    background: var(--paper);
    font-family: "Source Sans 3", "Myriad Pro", Arial, sans-serif;
  }
  .brand {
    position: absolute;
    left: 71px;
    top: 62px;
    display: flex;
    align-items: center;
    gap: 12px;
  }
  .brand-square {
    width: 34px;
    height: 34px;
    background: var(--accent);
  }
  .brand-name {
    font-size: 21px;
    font-weight: 600;
    letter-spacing: 1.5px;
    text-transform: uppercase;
    color: var(--brand-grey);
    line-height: 1;
  }
  .contact {
    position: absolute;
    right: 64px;
    top: 70px;
    text-align: right;
    font-size: 12px;
    line-height: 1;
    list-style: none;
  }
  .contact li { display: block; }
  .contact .phone   { color: var(--accent); margin-bottom: 6px; }
  .contact .email   { color: var(--accent); margin-bottom: 9px; }
  .contact .address { color: var(--ink-grey); font-size: 12.5px; margin-bottom: 9px; }
  .contact .web     { color: var(--accent); }
  .page-mark {
    position: absolute;
    left: 160px;
    top: 348px;
    width: 536px;
    height: 536px;
  }
</style>
</head>
<body>
  <main class="letterhead">
    <header>
      <div class="brand">
        <span class="brand-square" aria-hidden="true"></span>
        <span class="brand-name">Stratafold Projects</span>
      </div>
      <ul class="contact">
        <li class="phone">+1 234 567 89 00</li>
        <li class="email">info@emailaddress.com</li>
        <li class="address">physical address and location related information here</li>
        <li class="web">www.yourwebsite.com</li>
      </ul>
    </header>
    <svg class="page-mark" viewBox="0 0 536 536" aria-hidden="true">
      <circle cx="268" cy="268" r="262" fill="var(--mark-tint)"/>
      <circle cx="268" cy="268" r="222" fill="none" stroke="var(--mark-ring)" stroke-width="16"/>
    </svg>
  </main>
</body>
</html>
```